Harborline Ambulatory Flyer

Need to make a flyer similar to the attached Glenmark pdfs for Harborline Ambulatory. The write up is attached or can be found at https://www.velmontcareasc.com/bronx

Requirements
Must have
• What the existing flyer has.

```html
<!DOCTYPE html>
<html lang="en">
<head>
<meta charset="utf-8">
<title>Harborline Ambulatory Surgery Center – Flyer</title>
<link href="https://fonts.googleapis.com/css2?family=Montserrat:wght@400;500;600;700&display=swap" rel="stylesheet">
<style>
  :root {
    --blue: #2350a8;
    --blue-deep: #1c3f8c;
    --ink: #1b1b1b;
    --text: #2a2a2a;
    --panel: #f3f3f3;
    --paper: #ffffff;
    --backdrop: #c9c9c9;
    --footer: #0a0a0a;
    --icon-accent: #3d6fd0;
  }
  * { margin: 0; padding: 0; box-sizing: border-box; }
  html, body { width: 671px; height: 1200px; overflow: hidden; background: var(--backdrop); }
  body { font-family: "Montserrat", Arial, sans-serif; color: var(--text); position: relative; }

  .page {
    position: absolute; top: 381px;
    width: 624px; height: 876px;
    background: var(--paper);
    transform: scale(.5); transform-origin: 0 0;
    box-shadow: 0 2px 8px rgba(0,0,0,.12);
  }
  .page.front { left: 15px; }
  .page.back { left: 344px; }

  /* brand */
  .brand {
    position: absolute; left: 135px; top: 54px; width: 360px;
    text-align: center; font-weight: 700; color: var(--ink);
    text-transform: uppercase; line-height: 32px; font-size: 17px;
  }
  .brand-rule { position: absolute; left: 135px; top: 129px; width: 350px; height: 3px; background: var(--blue); }

  .hero-photo {
    position: absolute; left: 18px; top: 165px; width: 589px; height: 292px;
    background: linear-gradient(100deg, #2a4f9c 0%, #3a66b8 45%, #e9edf4 55%, #ffffff 68%, #eef1f6 80%, #2350a8 92%);
  }

  .services { position: absolute; top: 488px; list-style: none; }
  .services.left { left: 40px; }
  .services.right { left: 383px; }
  .services li {
    display: flex; align-items: center; height: 31px;
    font-size: 14px; font-weight: 500; letter-spacing: .4px; color: var(--ink);
  }
  .service-icon {
    width: 26px; height: 26px; border-radius: 50%;
    background: var(--blue); border: 2px solid #dbe3f3;
    box-shadow: 0 0 0 1px var(--blue);
    margin-right: 16px; flex: none;
  }
  .services-divider {
    position: absolute; left: 313px; top: 490px; height: 88px;
    border-left: 1.5px dotted #444;
  }

  .about-panel {
    position: absolute; left: 18px; top: 601px; width: 589px; height: 211px;
    background: var(--panel);
  }
  .about-copy {
    position: absolute; left: 20px; width: 314px;
    font-size: 10.6px; line-height: 1.26; text-align: justify; color: var(--text);
  }
  .about-copy.intro { top: 20px; }
  .about-copy.location { top: 137px; }
  .section-band {
    position: absolute; height: 36px;
    background: var(--blue); color: #fff;
    font-size: 10px; font-weight: 600; white-space: nowrap;
    display: flex; align-items: center; padding-left: 9px;
  }
  .about-panel .section-band { left: 20px; top: 84px; width: 314px; }
  .consult-photo {
    position: absolute; left: 370px; top: 18px; width: 196px; height: 172px;
    background: linear-gradient(135deg, #ffffff 0%, #f0f2f6 55%, #dde3ee 100%);
    border: 4px solid #fff; box-shadow: 0 1px 5px rgba(0,0,0,.18);
  }

  /* back page */
  .info-panel {
    position: absolute; left: 21px; top: 19px; width: 582px; height: 327px;
    background: var(--panel);
  }
  .info-panel .section-band { left: 17px; }
  .info-panel .band-capabilities { top: 11px; height: 34px; width: 383px; }
  .info-panel .band-benefits { top: 188px; height: 37px; width: 411px; }
  .info-copy {
    position: absolute; left: 19px; width: 544px;
    font-size: 10.4px; line-height: 13.5px; text-align: justify; color: var(--text);
  }
  .info-copy.capabilities { top: 55px; }
  .info-copy.benefits { top: 235px; }

  .offer-title {
    position: absolute; left: 40px; top: 364px;
    font-size: 10.5px; font-weight: 700; color: var(--blue);
  }
  .offer-rule { position: absolute; left: 103px; top: 371px; width: 169px; height: 3px; background: var(--blue); }
  .offer-panel {
    position: absolute; left: 35px; top: 388px; width: 263px; height: 257px;
    background: linear-gradient(180deg, #2656b0, var(--blue-deep));
    border-radius: 20px 0 20px 0;
  }
  .offer-list { list-style: none; position: absolute; left: 18px; top: 28px; }
  .offer-list li {
    display: flex; align-items: center; height: 35px;
    font-size: 13px; font-weight: 500; letter-spacing: .4px; color: #fff;
  }
  .offer-list .service-icon {
    width: 22px; height: 22px; margin-right: 17px;
    background: rgba(255,255,255,.18); border: 1.5px solid rgba(255,255,255,.5); box-shadow: none;
  }
  .surgery-room-photo {
    position: absolute; left: 325px; top: 388px; width: 263px; height: 257px;
    background: linear-gradient(180deg, #f4f6fa 0%, #e3e8f0 60%, #3a63b6 88%, #2350a8 100%);
    border: 1.5px solid var(--blue); border-radius: 0 20px 0 20px;
  }
  .brand.small { left: 45px; top: 704px; width: 210px; font-size: 11px; line-height: 21px; }
  .brand-rule.small { left: 39px; top: 756px; width: 217px; height: 2.5px; }
  .location-map {
    position: absolute; left: 305px; top: 677px; width: 264px; height: 114px;
    background: linear-gradient(135deg, #eeeeee, #d9d9d9);
  }

  /* footer */
  .contact-bar {
    position: absolute; left: 18px; top: 812px; width: 589px; height: 44px;
    background: var(--footer); color: #fff;
    display: flex; align-items: center;
  }
  .contact-item { display: flex; align-items: center; height: 100%; }
  .contact-item.address { width: 176px; padding-left: 22px; font-size: 10px; line-height: 1.2; }
  .contact-item.phone { width: 205px; justify-content: center; font-size: 15px; font-weight: 500; }
  .contact-item.online { flex: 1; padding-left: 14px; font-size: 10px; line-height: 1.6; }
  .contact-sep { height: 26px; border-left: 1.5px dotted #bbb; }
  .contact-item svg { flex: none; margin-right: 8px; }
  .online-row { display: flex; align-items: center; }
  .online-row svg { margin-right: 8px; }
</style>
</head>
<body>
  <main class="page front">
    <header>
      <div class="brand">Harborline<br>Ambulatory Surgery Center</div>
      <div class="brand-rule"></div>
    </header>

    <div class="hero-photo" role="img" aria-label="Two doctors in white coats with stethoscopes, arms crossed, in front of a blue-tinted operating room scene"></div>

    <ul class="services left">
      <li><span class="service-icon"></span>ORTHOPEDICS</li>
      <li><span class="service-icon"></span>PAIN MANAGEMENT</li>
      <li><span class="service-icon"></span>PODIATRY</li>
    </ul>
    <div class="services-divider"></div>
    <ul class="services right">
      <li><span class="service-icon"></span>OPHTHALMOLOGY</li>
      <li><span class="service-icon"></span>ENT &amp; PEDIATRIC ENT</li>
      <li><span class="service-icon"></span>GENERAL SURGERY</li>
    </ul>

    <section class="about-panel">
      <p class="about-copy intro">Harborline Ambulatory Surgery Center, is a same day surgical center, conveniently located in the Bronx, licensed by the state of New York and accredited by NAASC.</p>
      <h2 class="section-band">CONVENIENT LOCATION FOR PATIENTS &amp; SURGEONS</h2>
      <p class="about-copy location">Harborline Ambulatory Surgery Center is conveniently located on Calder Avenue in the Bronx, and is easily accessed from Manhattan, Westchester and Long Island with ample parking available on site.</p>
      <div class="consult-photo" role="img" aria-label="Close-up of a doctor writing notes with a pen at a bright white desk"></div>
    </section>

    <footer class="contact-bar">
      <div class="contact-item address">
        <svg width="13" height="16" viewBox="0 0 13 16"><path d="M6.5 0C2.9 0 0 2.8 0 6.3 0 10.8 6.5 16 6.5 16S13 10.8 13 6.3C13 2.8 10.1 0 6.5 0z" fill="#3d6fd0"/><circle cx="6.5" cy="6.2" r="2.4" fill="#000"/></svg>
        <span>2480 Calder Ave,<br>Bronx, NY 10458</span>
      </div>
      <div class="contact-sep"></div>
      <div class="contact-item phone">
        <svg width="14" height="14" viewBox="0 0 24 24"><path d="M6.6 10.8a15.1 15.1 0 0 0 6.6 6.6l2.2-2.2c.3-.3.7-.4 1-.2 1.1.4 2.3.6 3.6.6.6 0 1 .4 1 1V20c0 .6-.4 1-1 1A17 17 0 0 1 3 4c0-.6.4-1 1-1h3.5c.6 0 1 .4 1 1 0 1.3.2 2.5.6 3.6.1.3 0 .7-.2 1z" fill="#3d6fd0"/></svg>
        <span>(718) 555-0142</span>
      </div>
      <div class="contact-sep"></div>
      <div class="contact-item online">
        <div>
          <div class="online-row">
            <svg width="12" height="9" viewBox="0 0 12 9"><rect width="12" height="9" fill="#3d6fd0"/><path d="M0 0l6 5 6-5" fill="none" stroke="#000" stroke-width="1"/></svg>
            info@velmontcareasc.com
          </div>
          <div class="online-row">
            <svg width="12" height="12" viewBox="0 0 12 12"><circle cx="6" cy="6" r="5.5" fill="#3d6fd0"/><path d="M.5 6h11M6 .5v11" stroke="#000" stroke-width=".7" fill="none"/><ellipse cx="6" cy="6" rx="2.5" ry="5.5" fill="none" stroke="#000" stroke-width=".7"/></svg>
            www.velmontcareasc.com
          </div>
        </div>
      </div>
    </footer>
  </main>

  <main class="page back">
    <section class="info-panel">
      <h2 class="section-band band-capabilities">CAPABILITIES OF HARBORLINE AMBULATORY SURGERY CENTER</h2>
      <p class="info-copy capabilities">Harborline Ambulatory Surgery Center is a dedicated facility for same day procedures that do not require an overnight hospital stay, without sacrificing the quality of care and safety that a hospital provides. With over 15,000 sq ft of space and four operating rooms, the center offers specialties including orthopedics, pain management, podiatry, ophthalmology, ENT, pediatric ENT, and general surgery. These same day procedures, are performed by Harborline Ambulatory Surgery Center's highly skilled medical professionals that are committed to patient safety and satisfaction, providing the highest caliber of care with warmth and compassion in a personalized environment.</p>
      <h2 class="section-band band-benefits">BENEFITS OF CHOSING HARBORLINE AMBULATORY SURGERY CENTER</h2>
      <p class="info-copy benefits">More surgeons are choosing same day surgery centers because of the ability to provide high quality care in a state-of-the-art facility, at a more reasonable cost to you, your insurance provider, and your employer. Perhaps most importantly, same day surgery requires less down time, which means you'll spend less time away from your family and your job, and in most instances, you can return to your daily routine the next day.</p>
    </section>

    <h3 class="offer-title">WE OFFER</h3>
    <div class="offer-rule"></div>
    <section class="offer-panel">
      <ul class="offer-list">
        <li><span class="service-icon"></span>ORTHOPEDICS</li>
        <li><span class="service-icon"></span>PAIN MANAGEMENT</li>
        <li><span class="service-icon"></span>PODIATRY</li>
        <li><span class="service-icon"></span>OPHTHALMOLOGY</li>
        <li><span class="service-icon"></span>ADULT &amp; PEDIATRIC ENT</li>
        <li><span class="service-icon"></span>GENERAL SURGERY</li>
      </ul>
    </section>
    <div class="surgery-room-photo" role="img" aria-label="Bright modern operating room with monitors, lights and a blue surgical table"></div>

    <div class="brand small">Harborline<br>Ambulatory Surgery Center</div>
    <div class="brand-rule small"></div>
    <div class="location-map" role="img" aria-label="Street map of the surrounding Bronx neighborhood with the center's location marked"></div>

    <footer class="contact-bar">
      <div class="contact-item address">
        <svg width="13" height="16" viewBox="0 0 13 16"><path d="M6.5 0C2.9 0 0 2.8 0 6.3 0 10.8 6.5 16 6.5 16S13 10.8 13 6.3C13 2.8 10.1 0 6.5 0z" fill="#3d6fd0"/><circle cx="6.5" cy="6.2" r="2.4" fill="#000"/></svg>
        <span>2480 Calder Ave,<br>Bronx, NY 10458</span>
      </div>
      <div class="contact-sep"></div>
      <div class="contact-item phone">
        <svg width="14" height="14" viewBox="0 0 24 24"><path d="M6.6 10.8a15.1 15.1 0 0 0 6.6 6.6l2.2-2.2c.3-.3.7-.4 1-.2 1.1.4 2.3.6 3.6.6.6 0 1 .4 1 1V20c0 .6-.4 1-1 1A17 17 0 0 1 3 4c0-.6.4-1 1-1h3.5c.6 0 1 .4 1 1 0 1.3.2 2.5.6 3.6.1.3 0 .7-.2 1z" fill="#3d6fd0"/></svg>
        <span>(718) 555-0142</span>
      </div>
      <div class="contact-sep"></div>
      <div class="contact-item online">
        <div>
          <div class="online-row">
            <svg width="12" height="9" viewBox="0 0 12 9"><rect width="12" height="9" fill="#3d6fd0"/><path d="M0 0l6 5 6-5" fill="none" stroke="#000" stroke-width="1"/></svg>
            info@velmontcareasc.com
          </div>
          <div class="online-row">
            <svg width="12" height="12" viewBox="0 0 12 12"><circle cx="6" cy="6" r="5.5" fill="#3d6fd0"/><path d="M.5 6h11M6 .5v11" stroke="#000" stroke-width=".7" fill="none"/><ellipse cx="6" cy="6" rx="2.5" ry="5.5" fill="none" stroke="#000" stroke-width=".7"/></svg>
            www.velmontcareasc.com
          </div>
        </div>
      </div>
    </footer>
  </main>
</body>
</html>
```